Cat-products company needs smart, yet endearing, business card

We need a business card design for a new, but up-and-running, business based in Honolulu, Hawaii. The business is Purrlane Nest Co. Our first product is the most environmentally-friendly cat grass kit ever seen on the planet. Future products, currently in the R&D phase, will include a variety of exciting cat scratchers. We also do consulting work to help apartment-dwellers make their home more cat-friendly and, in the future, plan on doing full, custom installs of structure to create high walkways for cats.

Target Market(s)

Middle-aged, apartment-dwelling, middle-class workers who own 1 or more cats and who dote on them.

Industry/Entity Type

Pet Care

Contact Information for Business Card

A striking, professional, yet warm and friendly design is what we're after.

Font styles to use
Serif
Sans Serif
Other font styles liked:
• Comfortaa

Colors

Designer to choose colors to be used in the design.

Requirements
Must have
• The company logo: (see attachment)
• The company name: Purrlane Nest Co
• The web address: www.purrlanenestco.example
• Email: support@purrlanenestco.example
• Phone: +1 (808) 574 1630
• Update (Fri Jun 30 3017 7:45pm Hawaii Time) I would like, is possible, uploaded picture of the cat grass kit on the back of the card with some text along the lines of: Purrlane Nest Co - Maker Of The Freshest Cat Grass Kit Yet
Nice to have
• A cat picture, cartoon, real or silhouette that illustrates cats in action and/or relaxing; ie using the apartment space to live, play and relax in and being well-contented.
• Most of the website is done in the font: Comfortaa. It might be nice to continue using this for brand consistency.
Should not have
• Hard-to-read fonts.

```html
<!DOCTYPE html>
<html lang="en">
<head>
<meta charset="utf-8">
<title>Purrlane Nest Co – Business Card</title>
<link rel="stylesheet" href="https://fonts.googleapis.com/css2?family=Source+Sans+3:wght@400;600;800&display=swap">
<style>
  :root {
    --cocoa: #58352f;
    --marigold: #f6b012;
    --paper: #ffffff;
    --ink: #3b3331;
    --backdrop: #ece8e3;
    --text-font: "Source Sans 3", Arial, sans-serif;
  }
  * { margin: 0; padding: 0; box-sizing: border-box; }
  html, body {
    width: 1200px;
    height: 900px;
    overflow: hidden;
    background: var(--backdrop);
    font-family: var(--text-font);
  }
  .canvas { position: relative; width: 1200px; height: 900px; }

  .card {
    position: absolute;
    width: 560px;
    height: 320px;
    border-radius: 4px;
    overflow: hidden;
    box-shadow: 0 6px 18px rgba(60, 40, 30, 0.18);
  }

  /* Front */
  .card-front {
    left: 70px;
    top: 110px;
    background: var(--cocoa);
    display: flex;
    align-items: center;
    justify-content: center;
  }
  .brand-lockup {
    display: flex;
    align-items: center;
    gap: 16px;
  }
  .brand-dot {
    width: 34px;
    height: 34px;
    border-radius: 50%;
    background: var(--paper);
  }
  .brand-name {
    font-weight: 800;
    font-size: 44px;
    color: var(--marigold);
    letter-spacing: 0.5px;
  }

  /* Back */
  .card-back {
    left: 570px;
    top: 470px;
    background: var(--paper);
  }
  .back-wave {
    position: absolute;
    inset: 0;
  }
  .person {
    position: absolute;
    left: 50px;
    top: 46px;
  }
  .person-name {
    font-size: 22px;
    font-weight: 400;
    color: var(--marigold);
    text-transform: uppercase;
    letter-spacing: 0.3px;
    line-height: 1.1;
  }
  .person-role {
    font-size: 15px;
    color: var(--ink);
    margin-top: 2px;
  }
  .back-brand {
    position: absolute;
    right: 32px;
    top: 52px;
    display: flex;
    align-items: center;
    gap: 9px;
  }
  .back-brand .brand-square {
    width: 20px;
    height: 20px;
    background: var(--marigold);
  }
  .back-brand .brand-name {
    font-size: 26px;
    color: var(--cocoa);
  }
  .contact-list {
    position: absolute;
    left: 50px;
    top: 178px;
    list-style: none;
  }
  .contact-item {
    display: flex;
    align-items: center;
    gap: 9px;
    font-size: 15.5px;
    color: var(--ink);
    line-height: 1.45;
  }
  .contact-icon { width: 13px; height: 13px; flex: none; }
</style>
</head>
<body>
<main class="canvas">

  <section class="card card-front" aria-label="Card front">
    <div class="brand-lockup">
      <span class="brand-dot"></span>
      <span class="brand-name">Purrlane Nest Co</span>
    </div>
  </section>

  <section class="card card-back" aria-label="Card back">
    <svg class="back-wave" viewBox="0 0 560 320" width="560" height="320" aria-hidden="true">
      <path d="M0,262 C170,292 350,250 530,150 C370,262 190,300 0,282 Z" fill="var(--marigold)"/>
      <path d="M0,294 C190,318 390,262 560,150 L560,320 L0,320 Z" fill="var(--cocoa)"/>
    </svg>

    <div class="person">
      <p class="person-name">Marlowe Kealoha</p>
      <p class="person-role">Managing Director</p>
    </div>

    <div class="back-brand">
      <span class="brand-square"></span>
      <span class="brand-name">Purrlane Nest Co</span>
    </div>

    <ul class="contact-list">
      <li class="contact-item">
        <svg class="contact-icon" viewBox="0 0 16 16" aria-hidden="true">
          <path d="M3 1.5l3 .5 1 3.5-2 1.5c1 2 2.5 3.5 4.5 4.5l1.5-2 3.5 1 .5 3-2 1.5C7 15 1 9 1.5 3.5z" fill="var(--marigold)"/>
        </svg>
        <span>+1 (808) 574 1630</span>
      </li>
      <li class="contact-item">
        <svg class="contact-icon" viewBox="0 0 16 16" aria-hidden="true">
          <rect x="1" y="3" width="14" height="10" rx="1" fill="var(--marigold)"/>
          <path d="M1.5 4 8 9l6.5-5" fill="none" stroke="var(--paper)" stroke-width="1.3"/>
        </svg>
        <span>support@purrlanenestco.example</span>
      </li>
      <li class="contact-item">
        <svg class="contact-icon" viewBox="0 0 16 16" aria-hidden="true">
          <circle cx="8" cy="8" r="7" fill="var(--marigold)"/>
          <path d="M1 8h14M8 1c-3 3.5-3 10.5 0 14M8 1c3 3.5 3 10.5 0 14" fill="none" stroke="var(--paper)" stroke-width="1.1"/>
        </svg>
        <span>www.purrlanenestco.example</span>
      </li>
    </ul>
  </section>

</main>
</body>
</html>
```